MediBright Rx pharmacy / Local Independent Pharmacy

we need a logo with ( our staff picture on it ) for hometown pharmacy who treated patients as family , encourage customers to transfer their prescriptions to our pharmacy, delivering their medications for free and we accept all/most Insurances

Industry/Entity Type

Pharmaceutical

Colors
0054AA
0677BA
7BADD7
CADEEF
E8F1F8
EB3D1F
EC4F4E
F09395
F8D3D4
FCEDEE

Requirements
Must have
• THE PICTURE FOR THE STAFF , I DOWNLOADED TO THE PROJECT

```html
<!DOCTYPE html>
<html lang="en">
<head>
<meta charset="utf-8">
<title>MediBright Rx – Complete Pharmacy Needs</title>
<link rel="stylesheet" href="https://fonts.googleapis.com/css2?family=Anton&family=Oswald:wght@500;600&family=Barlow+Semi+Condensed:wght@700&display=swap">
<style>
  :root{
    --blue-deep:#0054AA;
    --blue:#0677BA;
    --blue-soft:#7BADD7;
    --blue-pale:#CADEEF;
    --ink-blue:#1D3F97;
    --red:#EB3D1F;
    --red-rose:#EC4F4E;
    --white:#FFFFFF;
    --ink:#111111;
  }
  *{margin:0;padding:0;box-sizing:border-box}
  html,body{width:1200px;height:448px;overflow:hidden;background:var(--white)}
  .banner{position:relative;width:1200px;height:448px;overflow:hidden;background:var(--white)}
  .backdrop{position:absolute;inset:0}
  .headline{position:absolute;color:var(--white);font-family:"Anton",sans-serif;line-height:1;
    white-space:nowrap;text-shadow:3px 3px 0 var(--ink-blue);font-weight:400}
  .headline--top{left:554px;top:23px;font-size:34px;letter-spacing:5px}
  .headline--main{left:536px;top:54px;font-size:98px;letter-spacing:8px}
  .headline--bottom{left:880px;top:158px;font-size:34px;letter-spacing:6px}
  .badge{position:absolute;left:1046px;top:22px;width:134px;height:132px}
  .badge__free{position:absolute;left:0;right:0;top:40px;text-align:center;color:var(--red);
    font-family:"Oswald",sans-serif;font-weight:600;font-size:40px;line-height:1;letter-spacing:1px}
  .badge__ribbon{position:absolute;left:9px;top:92px;width:116px;height:28px;background:var(--red);
    color:var(--white);font-family:"Oswald",sans-serif;font-weight:600;font-size:18px;line-height:28px;text-align:center}
  .phone{position:absolute;left:650px;top:224px;color:var(--white);font-family:"Oswald",sans-serif;
    font-weight:600;font-size:59px;line-height:1;letter-spacing:6px;white-space:nowrap}
  .phone-mark{position:absolute;left:558px;top:226px;width:58px;height:62px}
  .perks{position:absolute;left:458px;top:316px;list-style:none;color:var(--ink-blue);
    font-family:"Barlow Semi Condensed",sans-serif;font-weight:700;font-size:30px;line-height:40px;letter-spacing:.5px;white-space:nowrap}
  .perks li::before{content:"·";display:inline-block;width:18px;font-size:30px}
  .brand{position:absolute;left:982px;top:330px;display:flex;align-items:center;gap:8px;
    color:var(--red);font-family:"Oswald",sans-serif;font-weight:600;font-size:22px;line-height:1;white-space:nowrap}
  .brand__dot{width:22px;height:22px;border-radius:50%;background:var(--red)}
  .contact{position:absolute;left:950px;top:378px;color:var(--ink);font-family:"Oswald",sans-serif;
    font-weight:500;line-height:1;font-style:normal;white-space:nowrap}
  .contact__address{font-size:25px}
  .contact__web{font-size:24px;margin-top:5px}
</style>
</head>
<body>
<main class="banner">
  <svg class="backdrop" width="1200" height="448" viewBox="0 0 1200 448" aria-hidden="true">
    <defs>
      <radialGradient id="sky" cx="0.55" cy="0.75" r="0.9">
        <stop offset="0" stop-color="#CADEEF"/>
        <stop offset="0.45" stop-color="#7BADD7"/>
        <stop offset="1" stop-color="#0677BA"/>
      </radialGradient>
      <linearGradient id="whitefade" x1="0" y1="0" x2="0" y2="1">
        <stop offset="0" stop-color="#FFFFFF"/>
        <stop offset="1" stop-color="#F2F2F2"/>
      </linearGradient>
    </defs>
    <rect class="sky" x="0" y="0" width="1200" height="214" fill="url(#sky)"/>
    <rect class="phone-band" x="0" y="213" width="1200" height="89" fill="#EB3D1F"/>
    <rect class="footer" x="0" y="302" width="1200" height="146" fill="url(#whitefade)"/>
    <path class="photo-frame" d="M0,0 L455,0 C525,120 530,300 325,448 L0,448 Z" fill="#EC4F4E"/>
  </svg>

  <svg class="backdrop" width="1200" height="448" viewBox="0 0 1200 448">
    <defs>
      <linearGradient id="staffTones" x1="0" y1="0" x2="0" y2="1">
        <stop offset="0" stop-color="#C9C7C4"/>
        <stop offset="0.5" stop-color="#B7B3AE"/>
        <stop offset="1" stop-color="#EDEDEB"/>
      </linearGradient>
    </defs>
    <path class="staff-photo" role="img" aria-label="Photo of the three pharmacy staff in white coats standing in the store"
      d="M0,0 L443,0 C511,120 515,298 311,448 L0,448 Z" fill="url(#staffTones)"/>
  </svg>

  <h1>
    <span class="headline headline--top">COMPLETE</span>
    <span class="headline headline--main">PHARMACY</span>
    <span class="headline headline--bottom">NEEDS</span>
  </h1>

  <div class="badge">
    <svg width="134" height="132" viewBox="0 0 134 132" aria-hidden="true">
      <rect x="24" y="22" width="86" height="86" rx="12" transform="rotate(45 67 65)"
        fill="#FFFFFF" stroke="#1D3F97" stroke-width="2"/>
      <circle cx="60" cy="26" r="1.6" fill="#1D3F97"/>
      <circle cx="67" cy="26" r="1.6" fill="#1D3F97"/>
      <circle cx="74" cy="26" r="1.6" fill="#1D3F97"/>
    </svg>
    <span class="badge__free">FREE</span>
    <span class="badge__ribbon">Delivery</span>
  </div>

  <svg class="phone-mark" viewBox="0 0 58 62" role="img" aria-label="Medical emblem">
    <rect x="0" y="0" width="58" height="62" rx="6" fill="#EC4F4E"/>
  </svg>
  <p class="phone">765-555-0148</p>

  <ul class="perks">
    <li>We treat you as family.</li>
    <li>Easily transfer your prescription.</li>
    <li>We accept all/ most Insurances.</li>
  </ul>

  <div class="brand"><span class="brand__dot"></span><span class="brand__name">MediBright Rx</span></div>

  <address class="contact">
    <div class="contact__address">2150 N Maple Grove Rd</div>
    <div class="contact__web">www.medibrightrx.com</div>
  </address>
</main>
</body>
</html>
```